Ostrel Appraisals BV business cards (a financial services company)

I am looking for a business card design that stands out in the financial advisory field of business & intellectual property valuation. The business card design should be conservative, yet different. Address details have changed since the attached business card. New address is:

Molenvlietkade 27
4817 KT Leiden
The Netherlands

Telephone number remains the same.

```html
<!DOCTYPE html>
<html lang="en">
<head>
<meta charset="utf-8">
<title>Ostrel Appraisals BV – Business Cards</title>
<link href="https://fonts.googleapis.com/css2?family=Lato:wght@300;400;700&display=swap" rel="stylesheet">
<style>
  :root {
    --backdrop: #e6e6e6;
    --card-dark: #141414;
    --card-light: #ffffff;
    --ink-light: #f2f2f2;
    --ink-name: #6f6f6f;
    --ink-body: #4a4a4a;
    --ink-strong: #1e1e1e;
    --rule: #9a9a9a;
  }
  * { box-sizing: border-box; margin: 0; padding: 0; }
  html, body {
    width: 1200px; height: 716px; overflow: hidden;
    background: var(--backdrop);
    font-family: "Lato", "Helvetica Neue", Arial, sans-serif;
  }
  .stage {
    position: relative; width: 1200px; height: 716px;
    display: flex; align-items: center; justify-content: center; gap: 60px;
  }
  .card {
    position: relative; width: 500px; height: 300px;
    border-radius: 16px;
    box-shadow: 0 10px 30px rgba(0,0,0,.18);
  }
  /* Front */
  .card--front {
    background: var(--card-dark);
    display: flex; align-items: center; justify-content: center;
  }
  .wordmark {
    color: var(--ink-light);
    font-weight: 400; font-size: 26px; letter-spacing: 2px;
    text-transform: uppercase;
  }
  /* Back */
  .card--back { background: var(--card-light); color: var(--ink-body); }
  .identity { position: absolute; left: 36px; top: 34px; }
  .identity__name {
    font-size: 24px; font-weight: 300; letter-spacing: 1.5px;
    color: var(--ink-name); text-transform: uppercase;
  }
  .identity__creds {
    font-size: 13px; letter-spacing: 1px; text-transform: uppercase;
  }
  .identity__role {
    margin-top: 4px; font-size: 12px; font-weight: 700;
    letter-spacing: 1.6px; color: var(--ink-strong); text-transform: uppercase;
  }
  .divider {
    position: absolute; left: 36px; top: 106px; width: 280px; height: 1px;
    background: var(--rule);
  }
  .back-wordmark {
    position: absolute; right: 36px; top: 118px;
    font-size: 15px; font-weight: 400; letter-spacing: 1.5px;
    color: var(--ink-name); text-transform: uppercase;
  }
  .contacts {
    position: absolute; left: 36px; top: 148px; list-style: none;
    font-size: 12.5px; line-height: 22px;
  }
  .contacts li { display: flex; align-items: center; gap: 10px; }
  .contacts svg { width: 11px; height: 11px; fill: none; stroke: var(--ink-body); stroke-width: 1.4; }
  .address {
    position: absolute; right: 36px; bottom: 30px; text-align: right;
    font-style: normal; font-size: 12.5px; line-height: 19px;
  }
</style>
</head>
<body>
<main class="stage">
  <section class="card card--front" aria-label="Card front">
    <span class="wordmark">Ostrel Appraisals</span>
  </section>

  <section class="card card--back" aria-label="Card back">
    <header class="identity">
      <h1 class="identity__name">Marten Vos, <span class="identity__creds">CFA, ASA, RV</span></h1>
      <p class="identity__role">Managing Director</p>
    </header>
    <div class="divider"></div>
    <span class="back-wordmark">Ostrel Appraisals</span>

    <ul class="contacts">
      <li>
        <svg viewBox="0 0 12 12" aria-hidden="true"><path d="M3 1.5 L4.8 4 L3.8 5.2 Q5 7.3 6.8 8.2 L8 7.2 L10.5 9 L9.5 10.6 Q4.5 10 1.5 3 Z"/></svg>
        +31 (0)70 418 2263
      </li>
      <li>
        <svg viewBox="0 0 12 12" aria-hidden="true"><rect x="1" y="2.5" width="10" height="7"/><path d="M1 2.5 L6 6.5 L11 2.5"/></svg>
        mvos@ostrelappraisals.com
      </li>
      <li>
        <svg viewBox="0 0 12 12" aria-hidden="true"><circle cx="6" cy="6" r="4.8"/><path d="M1.2 6 H10.8 M6 1.2 Q3 6 6 10.8 M6 1.2 Q9 6 6 10.8"/></svg>
        www.ostrelappraisals.com
      </li>
    </ul>

    <address class="address">
      Molenvlietkade 27<br>
      4817 KT Leiden<br>
      The Netherlands
    </address>
  </section>
</main>
</body>
</html>
```